Career development coaching - school lever to adults, needs a business card

Tandel Grove - An independent Career Advice business that provides 1-2-1 advice,for career development, entrepreneurial support and workshops needs a business card. Our clients of all ages (school leaver to adults looking for a career move) and universities and colleges. We would like the card to be double-sided with a modern, professional look. Looking for something professional yet very creative and original. Want a standard size business card that inspires a second look because it stands out from the rest.

One side of the card to have a design incorporating the logo with Tandel Grove name with the strap line “Helping you find your future” and space for the company website

Other side of the card to the logo/Tandel Grove name and the usual contact information:
Individual Name
Job Title (for example, Director)
Phone number
Email address
Company website address

Facebook, LinkedIn and Twitter links will need to go somewhere (back or front!)

The design will be used for 3 individuals so should be editable so that we can update as needed/as we grow.

Attached is the company logo/colours to be incorporated.

Target Market(s)

1-2-1 advice,for career development, entrepreneurial support and workshops needs a business card. Our clients of all ages (school leaver to adults looking for a career move) and universities and colleges.

Industry/Entity Type

Consulting

Contact Information for Business Card

Individual Name
Phone number
Email address
Company website address

Font styles to use
Sans Serif

Colors
0255a3
3176b5
faa54b
f78f20
85acd3
cfdeed

Requirements
Must have
• use the Tandel Grove Logo in some way - using the colours and the blue/orange palette
• For the logo - hope this makes sense to someone or if they direclty relate to the logo image attached!
• For the Orange:- Pantone 1585 C
• In CMYK : C3 M71 Y100 K0
• For the Blue:- 100% Pantone 7469 C
• In CMYK : C100 M62 Y27 K7
• Please feel free to contact me with any questions for more info
Nice to have
• happy to see any creative designs
Should not have
• Nothing too traditional,

```html
<!DOCTYPE html>
<html lang="en">
<head>
<meta charset="utf-8">
<title>Tandel Grove — Business Card</title>
<link href="https://fonts.googleapis.com/css2?family=Roboto:wght@400;500&family=Khand:wght@500&display=swap" rel="stylesheet">
<style>
  :root {
    --stage: #ebebeb;
    --card-dark-top: #232323;
    --card-dark-bottom: #050505;
    --card-light: #f7f7f7;
    --blue: #1d5f86;
    --orange: #e8722e;
    --divider: #d6d6d6;
  }
  * { box-sizing: border-box; margin: 0; padding: 0; }
  html, body {
    width: 1200px; height: 443px; overflow: hidden;
    background: var(--stage);
  }
  .canvas { position: relative; width: 1200px; height: 443px; }

  .card {
    position: absolute;
    border-radius: 14px;
    overflow: hidden;
  }
  .card--front {
    left: 82px; top: 72px; width: 484px; height: 293px;
    background: linear-gradient(180deg, var(--card-dark-top), var(--card-dark-bottom));
  }
  .card--back {
    left: 602px; top: 71px; width: 482px; height: 291px;
    background: var(--card-light);
    border-bottom: 5px solid var(--blue);
  }

  .brand {
    position: absolute;
    display: flex; align-items: center; gap: 10px;
    font-family: "Roboto", sans-serif;
    font-weight: 500;
    color: var(--blue);
    letter-spacing: 0.5px;
    white-space: nowrap;
  }
  .brand__dot {
    border-radius: 50%;
    background: var(--orange);
    flex: none;
  }
  .card--front .brand {
    left: 50%; top: 50%; transform: translate(-50%, -50%);
    font-size: 26px;
  }
  .card--front .brand__dot { width: 30px; height: 30px; }
  .card--back .brand {
    left: 122px; top: 145px; transform: translate(-50%, -50%);
    font-size: 21px;
  }
  .card--back .brand__dot { width: 24px; height: 24px; }

  .divider {
    position: absolute; left: 226px; top: 65px;
    width: 1px; height: 148px; background: var(--divider);
  }

  .contact {
    position: absolute; left: 255px; top: 92px;
    font-family: "Roboto", sans-serif;
  }
  .contact__name {
    font-family: "Khand", sans-serif;
    font-weight: 500;
    font-size: 21px; line-height: 1;
    color: var(--orange);
  }
  .contact__role {
    margin-top: 6px;
    font-size: 11.5px; color: var(--blue);
  }
  .contact__list { list-style: none; margin-top: 20px; }
  .contact__item {
    display: flex; align-items: center; gap: 10px;
    font-size: 12.5px; line-height: 17.5px; color: var(--blue);
  }
  .contact__icon { width: 11px; height: 11px; flex: none; }
</style>
</head>
<body>
<main class="canvas">
  <section class="card card--front" aria-label="Card front">
    <div class="brand"><span class="brand__dot"></span>Tandel Grove</div>
  </section>

  <section class="card card--back" aria-label="Card back">
    <div class="brand"><span class="brand__dot"></span>Tandel Grove</div>
    <div class="divider"></div>
    <div class="contact">
      <p class="contact__name">Your Good Name</p>
      <p class="contact__role">Managing Director</p>
      <ul class="contact__list">
        <li class="contact__item">
          <svg class="contact__icon" viewBox="0 0 12 12" aria-hidden="true"><path fill="#e8722e" d="M1 4c0-2 2-3 5-3s5 1 5 3l-2 1-1-1.5H4L3 5 1 4zM3 6h6l1 5H2l1-5zm3 1.2a1.4 1.4 0 100 2.8 1.4 1.4 0 000-2.8z"/></svg>
          +00 111 22 33 44
        </li>
        <li class="contact__item">
          <svg class="contact__icon" viewBox="0 0 12 12" aria-hidden="true"><g fill="none" stroke="#e8722e" stroke-width="1.1"><circle cx="6" cy="6" r="5"/><ellipse cx="6" cy="6" rx="2.2" ry="5"/><path d="M1 6h10M2 3.3h8M2 8.7h8"/></g></svg>
          www.yourwebsite.com
        </li>
        <li class="contact__item">
          <svg class="contact__icon" viewBox="0 0 12 12" aria-hidden="true"><rect x="0.5" y="2" width="11" height="8" fill="#e8722e"/><path d="M0.8 2.4 6 6.6l5.2-4.2" fill="none" stroke="#f7f7f7" stroke-width="1"/></svg>
          yourname@yourwebsite.com
        </li>
      </ul>
    </div>
  </section>
</main>
</body>
</html>
```